Zielgruppe
Wir arbeiten in folgenden Bereichen:
- Mediation
- Konfliktmanagement
- Coaching
- Training
- Teamtraining
Über eine professionelle Webseite möchten wir neue Kunden gewinnen. Dazu möchten wir uns und unsere Leistungen vorstellen sowie dem Benutzer die Möglichkeit geben, sich über unsere anstehenden Projekte und Events zu informieren sowie uns zu kontaktieren.
Zielgruppe: Unsere Arbeit richtet sich an alle. Im Fokus stehen dabei Unternehmen. Theoretisch ist aber auch Arbeit mit Privatpersonen denkbar.
Aufgabenstellung
Farben: Dunkelblau, hellblau, weiß - Siehe Farben im PDF-Anhang. Eine weitere Akzentfarbe ist möglich.
Es geht ausschließlich um das Webdesign. Keine technische Umsetzung ist gewünscht.
Schriften: Bitte nur freie Schriften verwenden. Am besten wären Google Fonts.
Freie Stockfotos dürfen verwendet werden.
Das Design muss auf Desktop (optimiert auf ca. 1400px) und Mobile funktionieren (Responsive).
Nice to have wären optimierte App- und Favicons die auch vom Logo abweichen dürfen.
Die Seite wird mehrsprachig sein.
Für die Icons nur freie Icons verwenden.
Uns gefallen diese Seiten sehr gut. Es darf sich gern daran orientiert werden:
https://ufer-sieben.de/de/
https://bolmerhof.com
Wir wünschen uns ein komponentenbasiertes Design. Es soll uns möglich sein, die Komponenten frei zu kombinieren und neue Seiten zu kreieren. Als Vorgaben möchten wir gern die drei Seiten haben, die unten folgen.
Lieferung bitte in Figma. Das Resultat muss später in unseren Account übertragen werden können.

```html
<!DOCTYPE html>
<html lang="de">
<head>
<meta charset="utf-8">
<title>KlarWeg Mediation</title>
<link rel="stylesheet" href="https://fonts.googleapis.com/css2?family=Lexend:wght@300;400;500;600&display=swap">
<style>
:root{
  --dark:#13171d;
  --nav:#66abd8;
  --blue:#3f98d0;
  --card:#6cb1db;
  --page:#f5f4f7;
  --white:#ffffff;
  --text:#1d1f24;
  --yellow:#f3cb3e;
  --line:#b9d9ee;
}
*{box-sizing:border-box;margin:0;padding:0}
html,body{width:1200px;height:4530px;overflow:hidden}
body{position:relative;background:var(--page);font-family:'Lexend',sans-serif;color:var(--text)}
.abs{position:absolute}
.site-header{left:0;top:0;width:1200px;height:147px;background:var(--dark)}
.brand{display:flex;align-items:center;gap:16px;color:var(--white);font-family:'Lexend',sans-serif;font-weight:500;white-space:nowrap}
.brand-mark{width:34px;height:34px;background:var(--nav)}
.brand-header{left:0;width:1200px;justify-content:center;top:48px;font-size:44px}
.lang{right:24px;top:124px;color:#c8ccd2;font-size:12px;font-style:italic}
.main-nav{left:0;top:147px;width:1200px;height:64px;background:var(--nav);display:flex;justify-content:center;align-items:center;gap:48px;color:var(--white);font-size:19px;font-weight:300}
.hero{left:62px;top:290px;width:1067px;height:439px;background:linear-gradient(90deg,#3a3a3a,#8a8a8a 45%,#cfcfcf 60%,#5a5a5a)}
.hero-arrow{top:460px;width:40px;height:80px}
.welcome{left:57px;top:755px;font-size:24px}
.welcome-line{left:62px;top:797px;width:42px;height:3px;background:var(--yellow)}
.hello{color:var(--blue);font-weight:400;line-height:1}
.hello-big{font-size:80px}
.hello-sub{font-size:48px;font-weight:300;line-height:1.2}
.intro-title{left:62px;top:810px;width:310px}
.intro-title .hello-sub{font-size:46px;line-height:1.15}
.intro-text{left:391px;top:818px;width:536px;font-size:22px;line-height:31px;font-weight:300;text-align:justify}
.more{color:var(--yellow)}
.service-card{top:1077px;height:281px;background:var(--card);box-shadow:0 6px 10px rgba(0,0,0,.15);color:var(--white);display:flex;flex-direction:column;align-items:center}
.service-card svg{margin-top:30px;width:96px;height:96px}
.service-card span{margin-top:44px;font-size:32px;font-weight:400}
.team-photo{left:70px;top:1457px;width:675px;height:410px;background:linear-gradient(135deg,#8a4a33,#c7b3a2 45%,#f1f1ee 55%,#4a3a33)}
.team-title{left:795px;top:1440px}
.team-text{left:795px;top:1617px;width:330px;font-size:19.5px;line-height:24.5px;font-weight:300;text-align:justify}
.offer-box{left:70px;top:1925px;width:554px;height:597px;background:var(--white);border-bottom:3px solid var(--line)}
.offer{position:absolute;left:0;width:554px}
.offer svg{position:absolute;left:10px;top:10px;width:70px;height:60px}
.offer h3{position:absolute;left:116px;top:0;font-size:29px;font-weight:400;color:var(--blue)}
.offer p{position:absolute;left:116px;top:46px;width:300px;font-size:18px;line-height:24px;font-weight:300}
.values{left:672px;top:1955px;list-style:none}
.values li{height:99px;display:flex;align-items:flex-start;font-size:24px;font-weight:300}
.values svg{width:44px;height:44px;margin-right:33px;margin-top:-6px}
.events-title{left:79px;top:2600px}
.event-card{background:var(--white);border-bottom:3px solid var(--line)}
.event-card h3{font-size:32px;font-weight:400;color:var(--blue)}
.event-card p{font-size:18.5px;line-height:24.5px;font-weight:300;text-align:justify}
.btn{display:inline-block;width:152px;height:32px;border-radius:5px;background:var(--yellow);font-size:17px;text-align:center;line-height:32px;font-weight:300}
.contact-section{left:0;top:3478px;width:1200px;height:912px;background:var(--white)}
.label{left:75px;font-size:30px;font-weight:300}
.field{left:75px;width:584px;border:2px solid var(--blue);border-radius:40px}
.check{left:75px;top:4262px;width:46px;height:44px;border-radius:8px;background:var(--blue)}
.check-label{left:149px;top:4267px;font-size:28px;font-weight:300}
.contact-title{right:69px;top:3555px;text-align:right}
.desk-photo{left:705px;top:3713px;width:426px;height:611px;background:linear-gradient(160deg,#f2f2f2,#bdbdbd 45%,#3b3b3b 75%,#111)}
.site-footer{left:0;top:4390px;width:1200px;height:140px;background:var(--dark)}
.brand-footer{left:0;width:1200px;justify-content:center;top:4440px;font-size:40px}
.footer-links{right:29px;top:4414px;text-align:right;color:var(--white);font-size:24px;line-height:30px;font-weight:300}
</style>
</head>
<body>
<header class="abs site-header"></header>
<div class="abs brand brand-header"><span class="brand-mark"></span>KlarWeg Mediation</div>
<div class="abs lang">DE ⌄</div>
<nav class="abs main-nav">
  <span>MEDIATION, COACHING, TEAMTRAINING</span><span>ÜBER UNS</span><span>PROJEKTE &amp; EVENTS</span><span>KONTAKT</span>
</nav>

<div class="abs hero" role="img" aria-label="Schwarz-weißes Foto eines Handschlags zweier Geschäftsleute"></div>
<svg class="abs hero-arrow" style="left:84px" viewBox="0 0 40 80"><path d="M32 8 L8 40 L32 72" fill="none" stroke="#c9a93a" stroke-width="5"/></svg>
<svg class="abs hero-arrow" style="left:1062px" viewBox="0 0 40 80"><path d="M8 8 L32 40 L8 72" fill="none" stroke="#c9a93a" stroke-width="5"/></svg>

<div class="abs welcome">Willkommen!</div>
<div class="abs welcome-line"></div>
<div class="abs intro-title"><div class="hello hello-big">Hallo.</div><div class="hello hello-sub">Wir sind<br>KlarWeg<br>Mediation.</div></div>
<p class="abs intro-text">Lorem ipsum dolor sit amet, consectetur adipiscing elit. Nunc vulputate libero et velit interdum, ac aliquet odio mattis. Class aptent taciti sociosqu ad litora torquent per conubia nostra, per inceptos himenaeos. <span class="more">Mehr Details →</span></p>

<div class="abs service-card" style="left:62px;width:331px">
  <svg viewBox="0 0 96 96" fill="none" stroke="#fff" stroke-width="3"><path d="M30 80V62C18 54 16 40 22 28 30 12 58 10 70 24 78 34 78 50 66 60V80"/><path d="M44 30l-6 16h14l-8 18"/></svg>
  <span>MEDIATION</span>
</div>
<div class="abs service-card" style="left:431px;width:329px">
  <svg viewBox="0 0 96 96" fill="none" stroke="#fff" stroke-width="2.5"><rect x="50" y="12" width="22" height="18"/><circle cx="30" cy="24" r="6"/><circle cx="20" cy="64" r="6"/><circle cx="48" cy="64" r="6"/><circle cx="76" cy="64" r="6"/><path d="M10 84c0-8 20-8 20 0M38 84c0-8 20-8 20 0M66 84c0-8 20-8 20 0M30 30v14"/></svg>
  <span>COACHING</span>
</div>
<div class="abs service-card" style="left:795px;width:334px">
  <svg viewBox="0 0 96 96" fill="none" stroke="#fff" stroke-width="2.5"><circle cx="48" cy="48" r="7"/><circle cx="30" cy="58" r="6"/><circle cx="66" cy="58" r="6"/><path d="M20 80c0-8 20-8 20 0M56 80c0-8 20-8 20 0M38 68c0-8 20-8 20 0M20 10v16M48 10v16M76 10v16M14 20l6 6 6-6M42 20l6 6 6-6M70 20l6 6 6-6"/></svg>
  <span>TEAMTRAINING</span>
</div>

<div class="abs team-photo" role="img" aria-label="Foto der beiden Mediatoren vor einer Backsteinwand und einem Flipchart"></div>
<div class="abs team-title"><div class="hello hello-big">Hallo.</div><div class="hello hello-sub" style="margin-top:6px">Das sind wir.</div></div>
<p class="abs team-text">Lorem ipsum dolor sit amet, consectetur adipiscing elit. Nunc vulputate libero et velit interdum, ac aliquet odio mattis. Class aptent taciti sociosqu ad litora torquent per conubia nostra, per inceptos himenaeos. Class aptent taciti sociosqu ad litora torquent per conubia nostra, per inceptos himenaeos.</p>

<div class="abs offer-box">
  <div class="offer" style="top:30px"><svg viewBox="0 0 70 60" fill="none" stroke="#3f98d0" stroke-width="3"><rect x="4" y="6" width="20" height="12"/><rect x="40" y="30" width="24" height="14"/><path d="M14 18v24h26M4 52h20"/></svg><h3>Mediation</h3><p>Lorem ipsum dolor sit amet, consectetur adipiscing elit.</p></div>
  <div class="offer" style="top:173px"><svg viewBox="0 0 70 60" fill="none" stroke="#3f98d0" stroke-width="3"><rect x="26" y="6" width="36" height="22" rx="3"/><circle cx="18" cy="20" r="6"/><path d="M10 56V34l12-4 12-6M18 56V40"/></svg><h3>Vorträge</h3><p>Lorem ipsum dolor sit amet, consectetur adipiscing elit.</p></div>
  <div class="offer" style="top:325px"><svg viewBox="0 0 70 60" fill="none" stroke="#3f98d0" stroke-width="3"><rect x="12" y="4" width="12" height="28" rx="6"/><path d="M6 24c0 16 24 16 24 0M18 40v14"/></svg><h3>Training</h3><p>Lorem ipsum dolor sit amet, consectetur adipiscing elit.</p></div>
  <div class="offer" style="top:474px"><svg viewBox="0 0 70 60" fill="none" stroke="#3f98d0" stroke-width="3"><circle cx="22" cy="32" r="18"/><path d="M22 28v14M22 22v2"/></svg><h3>Beratung</h3><p>Lorem ipsum dolor sit amet, consectetur adipiscing elit.</p></div>
</div>

<ul class="abs values">
  <li><svg viewBox="0 0 44 44"><path d="M6 24l10 12L38 6" fill="none" stroke="#f3cb3e" stroke-width="4"/></svg>Verantwortungsbewusstsein</li>
  <li><svg viewBox="0 0 44 44"><path d="M6 24l10 12L38 6" fill="none" stroke="#f3cb3e" stroke-width="4"/></svg>Seriösität</li>
  <li><svg viewBox="0 0 44 44"><path d="M6 24l10 12L38 6" fill="none" stroke="#f3cb3e" stroke-width="4"/></svg>Engagement</li>
  <li><svg viewBox="0 0 44 44"><path d="M6 24l10 12L38 6" fill="none" stroke="#f3cb3e" stroke-width="4"/></svg>Zielorientiert</li>
  <li><svg viewBox="0 0 44 44"><path d="M6 24l10 12L38 6" fill="none" stroke="#f3cb3e" stroke-width="4"/></svg>Strategisch</li>
  <li><svg viewBox="0 0 44 44"><path d="M6 24l10 12L38 6" fill="none" stroke="#f3cb3e" stroke-width="4"/></svg>Bildend</li>
</ul>

<div class="abs events-title"><div class="hello hello-big">Hallo.</div><div class="hello hello-sub" style="margin-top:4px">Bock auf Events?</div></div>

<div class="abs event-card" style="left:75px;top:2795px;width:496px;height:294px;padding:22px">
  <h3>Business Coaching</h3>
  <p style="margin-top:6px">Lorem ipsum dolor sit amet, consectetur adipiscing elit. Nunc vulputate libero et velit interdum, ac aliquet odio mattis. Class aptent taciti sociosqu ad litora torquent per conubia nostra, per inceptos himenaeos.</p>
  <span class="btn" style="margin-top:38px">Buchen</span>
</div>
<div class="abs" style="left:576px;top:2795px;width:566px;height:294px;background:linear-gradient(180deg,#1c2024,#3b4248 45%,#14171a)" role="img" aria-label="Foto eines Vortrags vor Publikum in einer Halle"></div>

<div class="abs" style="left:75px;top:3133px;width:571px;height:294px;background:linear-gradient(90deg,#d0823d,#e9e6e2 40%,#c9c8c5 70%,#8a8f94)" role="img" aria-label="Foto zweier Frauen im Gespräch an einem Fenster"></div>
<div class="abs event-card" style="left:650px;top:3133px;width:492px;height:294px;padding:22px 30px 22px 38px;text-align:right">
  <h3>Private Coaching</h3>
  <p style="margin-top:26px">Lorem ipsum dolor sit amet, consectetur adipiscing elit. Nunc vulputate libero et velit interdum, ac aliquet odio mattis. Class aptent taciti sociosqu ad litora torquent per conubia nostra, per inceptos himenaeos.</p>
  <span class="btn" style="margin-top:26px">Buchen</span>
</div>

<section class="abs contact-section"></section>
<div class="abs label" style="top:3610px">Name</div>
<div class="abs field" style="top:3662px;height:66px"></div>
<div class="abs label" style="top:3759px">Email-Adresse</div>
<div class="abs field" style="top:3812px;height:66px"></div>
<div class="abs label" style="top:3902px">Nachricht</div>
<div class="abs field" style="top:3955px;height:252px"></div>
<div class="abs check"><svg viewBox="0 0 46 44" width="46" height="44"><path d="M12 22l8 8 14-14" fill="none" stroke="#fff" stroke-width="4"/></svg></div>
<div class="abs check-label">Abboniere den Newsletter.</div>
<svg class="abs" style="left:609px;top:4264px" width="52" height="42" viewBox="0 0 52 42"><path d="M3 3l46 18L3 39l8-18z M11 21h38" fill="none" stroke="#3f98d0" stroke-width="2.5" stroke-linejoin="round"/></svg>
<div class="abs contact-title"><div class="hello hello-big">Hallo.</div><div class="hello hello-sub" style="margin-top:2px">Get Connected.</div></div>
<div class="abs desk-photo" role="img" aria-label="Schwarz-weißes Foto einer Tastatur auf einem Schreibtisch"></div>

<footer class="abs site-footer"></footer>
<div class="abs brand brand-footer"><span class="brand-mark"></span>KlarWeg Mediation</div>
<div class="abs footer-links">Impressum<br>Datenschutz<br>Kontakt</div>
</body>
</html>
```